Tranquil Renewal

Medical doctor providing aesthetic medicine

* Double sided card
* Logo to be on card
Other details:
* Dr. Halvard Meckin, BSc, MBChB, CCFP
* #214-215, 27394 83 Ave, Surrey, BC, V4T 2K7
* 604-718-2453
* info@calmbrookclinic.ca
* www.calmbrookclinic.ca

Industry/Entity Type

Medical / Health & Beauty

Contact Information for Business Card

see 'Project Description'

Colors
0054AA
0677BA
7BADD7
CADEEF
E8F1F8
FFF300
FFF600
FEFA6F
FFFEC7
FFFEE8

Requirements
Must have
• Modern, high-end design

```html
<!DOCTYPE html>
<html lang="en">
<head>
<meta charset="utf-8">
<title>Tranquil Renewal – Business Card</title>
<link href="https://fonts.googleapis.com/css2?family=Poppins:wght@300;400;600&display=swap" rel="stylesheet">
<style>
  :root {
    --backdrop: #222223;
    --card-dark: #1f1f22;
    --gold: #d4a53a;
    --gold-deep: #b98a33;
    --gold-bright: #e6c02a;
    --gold-soft: #c9a23c;
    --ink-light: #f2f2f2;
    --ink-muted: #d8d8d8;
  }
  * { margin: 0; padding: 0; box-sizing: border-box; }
  html, body {
    width: 1200px; height: 780px; overflow: hidden;
    background: var(--backdrop);
    font-family: "Poppins", sans-serif;
  }
  .stage {
    position: relative; width: 1200px; height: 780px;
    display: flex; align-items: center; justify-content: center; gap: 40px;
  }
  .card {
    position: relative; width: 560px; height: 320px; overflow: hidden;
    box-shadow: 0 14px 30px rgba(0,0,0,0.5);
  }

  /* Front */
  .card-front { background: var(--card-dark); }
  .brand-name {
    position: absolute; left: 52px; top: 112px;
    font-weight: 400; font-size: 24px; line-height: 1.25;
    color: var(--ink-light);
  }
  .divider { position: absolute; left: 0; top: 0; }
  .contact {
    position: absolute; left: 320px; top: 58px; color: var(--ink-light);
  }
  .doctor-name { font-size: 22px; font-weight: 300; line-height: 1.1; }
  .doctor-name .first { font-weight: 600; color: var(--gold); }
  .credentials { font-size: 11.5px; font-weight: 300; margin-top: 4px; color: var(--ink-muted); }
  .contact-list { list-style: none; margin-top: 20px; }
  .contact-list li {
    display: flex; align-items: center; gap: 9px;
    font-size: 11.5px; font-weight: 300; margin-bottom: 7px;
  }
  .contact-list svg { width: 13px; height: 13px; flex: none; }
  .address-band {
    position: absolute; left: 0; bottom: 34px; width: 520px; height: 30px;
    background: linear-gradient(90deg, var(--gold-deep), var(--gold-bright) 55%, var(--gold-deep));
    display: flex; align-items: center; justify-content: center;
    font-size: 13px; font-weight: 400; color: #ffffff; letter-spacing: 0.2px;
  }
  .band-tab {
    position: absolute; right: 0; bottom: 64px; width: 40px; height: 24px;
    background: #ffffff;
  }

  /* Back */
  .card-back { background: var(--gold-bright); }
  .back-pattern {
    position: absolute; inset: 0;
    background: linear-gradient(160deg, #d9b42a 0%, #e8c52a 45%, #d3ad2e 100%);
  }
  .back-brand {
    position: absolute; right: 28px; bottom: 24px;
    font-size: 11px; font-weight: 400; color: #ffffff;
  }
</style>
</head>
<body>
<main class="stage">

  <section class="card card-front" aria-label="Business card front">
    <p class="brand-name">Tranquil<br>Renewal</p>

    <svg class="divider" width="560" height="320" viewBox="0 0 560 320" aria-hidden="true">
      <line x1="250" y1="40" x2="300" y2="220" stroke="var(--gold)" stroke-width="1"/>
    </svg>

    <div class="contact">
      <p class="doctor-name"><span class="first">Dr. Halvard</span> Meckin</p>
      <p class="credentials">BSc, MBChB, CCFP</p>
      <ul class="contact-list">
        <li>
          <svg viewBox="0 0 24 24" aria-hidden="true"><path fill="var(--gold)" d="M6.6 10.8a15.1 15.1 0 0 0 6.6 6.6l2.2-2.2a1 1 0 0 1 1-.25 11.4 11.4 0 0 0 3.6.57 1 1 0 0 1 1 1V20a1 1 0 0 1-1 1A17 17 0 0 1 3 4a1 1 0 0 1 1-1h3.5a1 1 0 0 1 1 1c0 1.25.2 2.45.57 3.57a1 1 0 0 1-.25 1z"/></svg>
          604-718-2453
        </li>
        <li>
          <svg viewBox="0 0 24 24" aria-hidden="true"><rect x="2" y="5" width="20" height="14" rx="1.5" fill="none" stroke="var(--gold)" stroke-width="2"/><path d="M3 6l9 7 9-7" fill="none" stroke="var(--gold)" stroke-width="2"/></svg>
          info@calmbrookclinic.ca
        </li>
        <li>
          <svg viewBox="0 0 24 24" aria-hidden="true"><circle cx="12" cy="12" r="9" fill="none" stroke="var(--gold)" stroke-width="2"/><path d="M3 12h18M12 3c3 3.2 3 14.8 0 18M12 3c-3 3.2-3 14.8 0 18" fill="none" stroke="var(--gold)" stroke-width="1.6"/></svg>
          www.calmbrookclinic.ca
        </li>
      </ul>
    </div>

    <div class="band-tab"></div>
    <div class="address-band">#214-215, 27394 83 Ave, Surrey, BC, V4T 2K7</div>
  </section>

  <section class="card card-back" aria-label="Business card back">
    <div class="back-pattern" role="img" aria-label="Repeating embossed pattern in gold tones"></div>
    <p class="back-brand">Tranquil Renewal</p>
  </section>

</main>
</body>
</html>
```